Auto glazing business card design

need a business card design for my company, the logo will be provided with an inspirational design as well.
It is for an auto glazing business in Australia.
I would like to have the basic details on the card as my name, phone number, email adress and website.
I suppose the challenge will be to fit a long email adress on a small business card.

Target Market(s)

autoglazing customers, retail mostly

Industry/Entity Type

auto glazing

Contact Information for Business Card

logo, name, phone, email and website

Colors
0054AA
0677BA
7BADD7
CADEEF
E8F1F8
0094D4
00A9DD
6FCCEA
C7EBF8
E9F6FB

Requirements
Must have
• logo, business details, maybe QR code

```html
<!DOCTYPE html>
<html lang="en">
<head>
<meta charset="utf-8">
<title>Clearview Mobile Glazing – Business Card</title>
<link href="https://fonts.googleapis.com/css2?family=Lato:wght@400;700;900&display=swap" rel="stylesheet">
<style>
  :root {
    --backdrop: #8f8f8f;
    --card: #ffffff;
    --navy: #0c1a33;
    --teal: #1a8db3;
    --blue-deep: #0a5e98;
    --blue-mid: #0b7ca6;
    --aqua-light: #52c3d0;
    --text: #2b2f36;
  }
  * { box-sizing: border-box; margin: 0; padding: 0; }
  html, body {
    width: 1200px; height: 1000px; overflow: hidden;
    background: var(--backdrop);
    font-family: "Lato", Arial, sans-serif;
  }
  .stage { position: relative; width: 1200px; height: 1000px; }
  .card {
    position: absolute; left: 290px; width: 629px; height: 359px;
    background: var(--card); border-radius: 22px; overflow: hidden;
    box-shadow: 0 2px 4px rgba(0,0,0,0.25);
  }
  .card--front { top: 97px; }
  .card--back { top: 532px; }
  .card__deco { position: absolute; top: 0; left: 0; width: 629px; height: 359px; }

  .holder { position: absolute; left: 63px; top: 64px; }
  .holder__name {
    font-weight: 900; font-size: 29px; letter-spacing: 0.3px;
    color: var(--navy); line-height: 1;
  }
  .holder__title {
    font-size: 16px; color: var(--teal); margin-top: 5px; letter-spacing: 0.2px;
  }
  .holder__rule {
    width: 35px; height: 3px; background: var(--navy); margin: 14px 0 0 2px;
  }
  .contact { position: absolute; left: 63px; top: 148px; list-style: none; }
  .contact__item {
    display: flex; align-items: flex-start; gap: 10px;
    font-size: 15px; color: var(--text); line-height: 19.5px; letter-spacing: 0.2px;
  }
  .contact__item--address { margin-bottom: 6px; }
  .contact__icon { width: 12px; height: 12px; margin-top: 4px; flex: none; fill: var(--teal); }

  .brand {
    position: absolute; left: 270px; top: 200px; width: 280px;
    text-align: center; color: var(--navy); font-weight: 700;
  }
  .brand__main { font-size: 32px; letter-spacing: 7px; line-height: 1; }
  .brand__sub { font-size: 13px; letter-spacing: 7px; margin-top: 10px; }
</style>
</head>
<body>
<main class="stage">

  <section class="card card--front" aria-label="Business card front">
    <svg class="card__deco" viewBox="0 0 629 359" aria-hidden="true">
      <defs>
        <linearGradient id="frontBand" x1="0" y1="0" x2="1" y2="0">
          <stop offset="0" stop-color="var(--blue-deep)"/>
          <stop offset="1" stop-color="var(--teal)"/>
        </linearGradient>
      </defs>
      <rect x="520" y="0" width="109" height="359" fill="url(#frontBand)"/>
      <rect x="500" y="0" width="5" height="359" fill="var(--teal)"/>
    </svg>

    <div class="holder">
      <h1 class="holder__name">DANIEL HARTLEY</h1>
      <p class="holder__title">Founder &amp; CEO</p>
      <div class="holder__rule"></div>
    </div>

    <ul class="contact">
      <li class="contact__item contact__item--address">
        <svg class="contact__icon" viewBox="0 0 12 12"><path d="M6 0a4 4 0 0 0-4 4c0 3 4 8 4 8s4-5 4-8a4 4 0 0 0-4-4zm0 5.5A1.5 1.5 0 1 1 6 2.5a1.5 1.5 0 0 1 0 3z"/></svg>
        <span>Street Address Here, City<br>State, Country, ZIP 123</span>
      </li>
      <li class="contact__item">
        <svg class="contact__icon" viewBox="0 0 12 12"><path d="M2.5 0.5l2 2.5-1 1.2c.7 1.5 1.8 2.6 3.3 3.3l1.2-1 2.5 2-1.2 2C5 10.2 1.8 7 .5 1.7z"/></svg>
        <span>(123) 456-7890</span>
      </li>
      <li class="contact__item">
        <svg class="contact__icon" viewBox="0 0 12 12"><path d="M3 0h6a1 1 0 0 1 1 1v10a1 1 0 0 1-1 1H3a1 1 0 0 1-1-1V1a1 1 0 0 1 1-1zm.5 1.5v7.5h5V1.5z"/></svg>
        <span>(123) 456-7890</span>
      </li>
      <li class="contact__item">
        <svg class="contact__icon" viewBox="0 0 12 12"><path d="M3 0h6v3H3zM1 4h10a1 1 0 0 1 1 1v4H10v3H2V9H0V5a1 1 0 0 1 1-1zm2.5 4.5v2h5v-2z"/></svg>
        <span>(123) 456-7890</span>
      </li>
      <li class="contact__item">
        <svg class="contact__icon" viewBox="0 0 12 12"><path d="M0 2h12v8H0zm1.2 1L6 6.5 10.8 3z"/></svg>
        <span>info@clearviewmobileglazing.com</span>
      </li>
      <li class="contact__item">
        <svg class="contact__icon" viewBox="0 0 12 12"><path d="M6 0a6 6 0 1 0 0 12A6 6 0 0 0 6 0zm0 1.2a4.8 4.8 0 0 1 4.5 3.2H8.2L7 3H5zM1.3 6.5h2l1.5 1.5v2.6A4.8 4.8 0 0 1 1.3 6.5z"/></svg>
        <span>clearviewmobileglazing.com</span>
      </li>
    </ul>
  </section>

  <section class="card card--back" aria-label="Business card back">
    <svg class="card__deco" viewBox="0 0 629 359" aria-hidden="true">
      <defs>
        <linearGradient id="backBand" x1="0" y1="0" x2="1" y2="0">
          <stop offset="0" stop-color="var(--teal)"/>
          <stop offset="1" stop-color="var(--aqua-light)"/>
        </linearGradient>
      </defs>
      <rect x="0" y="0" width="130" height="359" fill="url(#backBand)"/>
      <rect x="145" y="0" width="5" height="359" fill="var(--teal)"/>
    </svg>

    <div class="brand">
      <p class="brand__main">CLEARVIEW</p>
      <p class="brand__sub">MOBILE GLAZING</p>
    </div>
  </section>

</main>
</body>
</html>
```